The Wellness Barn Business Card

Info for the front..... (in whichever order and layout looks best)
Carla Penhallow
Physiotherapist
4/37 Upper Creekbank Rd
Tallowbrook
QLD 4712
0462305178
carlapenhallow57@mailbox.example
www.thewellnessbarn.example.au
on the back I would like to be able to write appointments so probably just that heading with lines.
I like a sort of rustic style but mostly professional, colours in naturals, beige, brown, green etc. I dont mind if the logo colour is changed slightly to suit.

```html
<!DOCTYPE html>
<html lang="en">
<head>
<meta charset="utf-8">
<title>The Wellness Barn – Business Card</title>
<link href="https://fonts.googleapis.com/css2?family=Open+Sans:wght@400;600;700&display=swap" rel="stylesheet">
<style>
  :root {
    --backdrop: #3a3a3a;
    --paper-light: #ece7dc;
    --paper-mid: #e0d8c6;
    --paper-edge: #cbbd9c;
    --green: #2f5322;
    --brown: #7a6a44;
    --line-green: #3d5a2c;
    --icon: #8a8068;
  }
  * { margin: 0; padding: 0; box-sizing: border-box; }
  html, body {
    width: 1200px; height: 900px; overflow: hidden;
    background: var(--backdrop);
    font-family: "Open Sans", Arial, sans-serif;
  }
  .canvas {
    width: 1200px; height: 900px;
    display: flex; flex-direction: column;
    align-items: center; justify-content: center; gap: 44px;
  }
  .card {
    position: relative;
    width: 665px; height: 380px;
    background:
      radial-gradient(ellipse at 45% 40%, var(--paper-light) 0%, var(--paper-mid) 60%, var(--paper-edge) 120%);
    box-shadow: 0 10px 24px rgba(0,0,0,.45);
  }
  .brand {
    position: absolute; top: 42px; right: 44px;
    color: var(--green);
    font-weight: 700; font-size: 34px; line-height: 1.05;
    text-align: right;
  }
  .card-back .date-line, .card-back .appointment-rule { position: absolute; }
  .appointment {
    position: absolute; left: 40px; right: 40px; top: 232px;
    display: flex; align-items: flex-end; gap: 8px;
  }
  .appointment-label { color: var(--green); font-weight: 700; font-size: 19px; white-space: nowrap; }
  .rule-solid { flex: 1; border-bottom: 1.5px solid var(--line-green); margin-bottom: 5px; }
  .schedule {
    position: absolute; left: 40px; right: 40px; top: 296px;
    display: flex; align-items: flex-end; gap: 8px;
    color: var(--brown); font-weight: 700; font-size: 17px;
  }
  .rule-dotted { flex: 1; border-bottom: 3px dotted var(--brown); margin-bottom: 5px; }
  .identity {
    position: absolute; left: 40px; right: 40px; top: 190px;
  }
  .person-name { color: var(--brown); font-weight: 700; font-size: 19px; }
  .role-row { display: flex; align-items: flex-end; gap: 8px; }
  .person-role { color: var(--green); font-size: 16px; white-space: nowrap; }
  .contacts {
    position: absolute; left: 40px; top: 262px;
    list-style: none; color: var(--green); font-size: 16px;
  }
  .contacts li { display: flex; align-items: center; gap: 10px; height: 24px; }
  .contacts svg { width: 16px; height: 16px; fill: none; stroke: var(--icon); stroke-width: 2; flex: none; }
  .contacts svg .solid { fill: var(--icon); stroke: none; }
</style>
</head>
<body>
<main class="canvas">

  <section class="card card-back" aria-label="Appointment side">
    <div class="brand">The Wellness<br>Barn</div>
    <div class="appointment">
      <span class="appointment-label">Your Appointment</span>
      <span class="rule-solid"></span>
    </div>
    <div class="schedule">
      <span>Date</span><span class="rule-dotted"></span>
      <span>Time</span><span class="rule-dotted"></span>
    </div>
  </section>

  <section class="card card-front" aria-label="Contact side">
    <div class="brand">The Wellness<br>Barn</div>
    <div class="identity">
      <p class="person-name">Carla Penhallow</p>
      <div class="role-row">
        <span class="person-role">Physiotherapist</span>
        <span class="rule-solid"></span>
      </div>
    </div>
    <ul class="contacts">
      <li>
        <svg viewBox="0 0 16 16" aria-hidden="true"><path class="solid" d="M3 1.5l2.5-.5 1.5 3.5-1.7 1.2a8 8 0 0 0 4.5 4.5l1.2-1.7 3.5 1.5-.5 2.5c-.3 1-1.3 1.5-2.3 1.3A12 12 0 0 1 1.2 3.8C1 2.8 2 1.8 3 1.5z"/></svg>
        <span>0462305178</span>
      </li>
      <li>
        <svg viewBox="0 0 16 16" aria-hidden="true"><rect x="1.5" y="3.5" width="13" height="9"/><path d="M1.5 3.5l6.5 5.5 6.5-5.5"/></svg>
        <span>carlapenhallow57@mailbox.example</span>
      </li>
      <li>
        <svg viewBox="0 0 16 16" aria-hidden="true"><circle cx="8" cy="8" r="6.5"/><ellipse cx="8" cy="8" rx="3" ry="6.5"/><path d="M1.5 8h13M2.5 4.8h11M2.5 11.2h11"/></svg>
        <span>www.thewellnessbarn.example.au</span>
      </li>
      <li>
        <svg viewBox="0 0 16 16" aria-hidden="true"><path class="solid" d="M8 .8a5 5 0 0 0-5 5c0 3.8 5 9.4 5 9.4s5-5.6 5-9.4a5 5 0 0 0-5-5zm0 7a2 2 0 1 1 0-4 2 2 0 0 1 0 4z"/></svg>
        <span>4/37 Upper Creekbank Rd, Tallowbrook, QLD 4712</span>
      </li>
    </ul>
  </section>

</main>
</body>
</html>
```